Valdarossi’s Artisan Pizzeria Menu Contest

I’m looking for a menu design for a new pizzeria - it’s farm to table type of restaurant - more upscale than a typical pizzeria - white washed wood interior with some industrial accents - I am looking for a creative menu layout using the attached sample menu items -
Valdarossi’s is an artisanal pizzeria with an atmosphere that will make you feel at home for any situation, first date, anniversary, business lunch, boys night out or girls night out with a menu inspired by the idea of a simple honest cooking paired with fresh – quality ingredients. Full service dining experience that is still casual but dedicated to extraordinary hospitality.
While developing the menu we have created a network of amazing farms and purveyors to supply our restaurant with fresh milled 100% California flour for our hand crafted dough, as well as sustainably farmed organic produce, meats and cheeses.
The menu includes classics like the Margherita pizza to daily seasonal specials, fresh salads to rustic small plates including moms meatball recipe to a fresh local burrata with handmade bread. Each dish reflects our passion for sourcing the freshest quality local ingredients.
To compliment the menu, Valdarossi’s serves an extensive wine list with selections focusing on Italian varietals. The cocktail program has been carefully crafted to offer something to entice ever palate and the beer list has unique selections of the world’s finest brewers.
Target Market(s)
25-45 year old men and women
Industry/Entity Type
American Restaurant
Requirements
Must have
- professional tone
Nice to have
- a balance of elegance and industrial (rustic)
Should not have
- photos or playful graphics etc..

```html
<!DOCTYPE html>
<html lang="en">
<head>
<meta charset="utf-8">
<title>Valdarossi’s Artisan Pizzeria – Menu</title>
<link href="https://fonts.googleapis.com/css2?family=Oswald:wght@500&family=Signika:wght@400&display=swap" rel="stylesheet">
<style>
  :root {
    --menu-red: #e3334a;
    --ink-white: #ffffff;
    --ink-dark: #1b1b1b;
    --linen: #e8e8e6;
    --page: #ffffff;
    --decor: rgba(255,255,255,0.12);
    --head-font: "Oswald", "Arial Narrow", sans-serif;
    --body-font: "Signika", "Trebuchet MS", sans-serif;
  }
  * { margin: 0; padding: 0; box-sizing: border-box; }
  html, body { width: 1200px; height: 1000px; overflow: hidden; background: var(--page); }
  .canvas { position: relative; width: 1200px; height: 1000px; background: var(--page); font-family: var(--body-font); color: var(--ink-white); }
  .linen-band { position: absolute; left: 0; top: 78px; width: 1200px; height: 844px; background: var(--linen); }

  .panel {
    position: absolute; background: var(--menu-red); border-radius: 16px;
    box-shadow: inset 0 0 0 6px var(--menu-red), inset 0 0 0 8px var(--ink-white);
  }
  .panel--starters { left: 12px; top: 145px; width: 375px; height: 770px; }
  .panel--pizzas { left: 413px; top: 88px; width: 374px; height: 827px; }
  .panel--more { left: 813px; top: 88px; width: 375px; height: 827px; }

  .section-head {
    position: absolute; left: 16px; right: 16px; height: 14px;
    border: 2px solid var(--ink-white); border-bottom: none;
  }
  .section-head__pill {
    position: absolute; left: 50%; top: -14px; transform: translateX(-50%);
    background: var(--ink-white); color: var(--ink-dark); border-radius: 12px;
    height: 28px; padding: 0 22px; display: flex; align-items: center; gap: 10px;
    font-family: var(--head-font); font-weight: 500; font-size: 20px; white-space: nowrap;
  }
  .section-head__pill::before, .section-head__pill::after {
    content: ""; width: 5px; height: 5px; border-radius: 50%; background: var(--menu-red);
  }
  .section-head--large .section-head__pill { top: -19px; height: 38px; font-size: 30px; padding: 0 20px; }
  .section-head--small .section-head__pill { font-size: 17px; }

  .item { position: absolute; left: 27px; right: 30px; }
  .item__name { font-size: 17px; font-weight: 400; line-height: 19px; }
  .item__price { position: absolute; right: 0; top: 0; font-size: 17px; line-height: 19px; }
  .item__desc { width: 205px; font-size: 9.5px; line-height: 11.5px; text-align: justify; }
  .item--plain .item__name { font-size: 17px; }

  .decor { position: absolute; background: var(--decor); border-radius: 50%; }

  .brand-badge {
    position: absolute; left: 98px; top: 82px; width: 202px; height: 106px;
    background: var(--ink-dark); border-radius: 14px;
    box-shadow: inset 0 0 0 4px var(--ink-dark), inset 0 0 0 6px var(--ink-white);
    display: flex; align-items: center; justify-content: center;
  }
  .brand-name { font-family: var(--head-font); font-weight: 500; color: var(--ink-white); font-size: 34px; letter-spacing: 1px; }
  .brand-footer { position: absolute; left: 0; right: 0; top: 744px; text-align: center; }
  .brand-footer .brand-name { font-size: 40px; }
</style>
</head>
<body>
<div class="canvas">
  <div class="linen-band"></div>

  <!-- Left column -->
  <section class="panel panel--starters">
    <div class="section-head" style="top:75px"><span class="section-head__pill">APPETIZERS</span></div>
    <div class="item" style="top:95px"><h3 class="item__name">Brussels</h3><span class="item__price">$10,00</span><p class="item__desc">Pan seared brussel sprouts with a drizzle of balsamic reduction and parm and bread crumbs</p></div>
    <div class="item" style="top:151px"><h3 class="item__name">Meatballs</h3><span class="item__price">$13,00</span><p class="item__desc">Moms meatballs handmade secret recipe for over 75 years</p></div>
    <div class="item" style="top:195px"><h3 class="item__name">Mussels</h3><span class="item__price">$15,00</span><p class="item__desc">New Zealand Mussels in a tomato broth</p></div>
    <div class="item" style="top:227px"><h3 class="item__name">Romanesco</h3><span class="item__price">$11,00</span><p class="item__desc">Flash fried romanesco served atop a spicy aioli</p></div>
    <div class="item" style="top:271px"><h3 class="item__name">Chicken wings</h3><span class="item__price">$10,00</span><p class="item__desc">Italian fried chicken wings with a kick</p></div>
    <div class="item" style="top:303px"><h3 class="item__name">Burrata</h3><span class="item__price">$13,00</span><p class="item__desc">Local burrata served with apples grapes and fresh made bread</p></div>
    <div class="decor" role="img" aria-label="Faint appetizer icon" style="left:153px;top:355px;width:65px;height:50px"></div>

    <div class="section-head" style="top:440px"><span class="section-head__pill">SALADS</span></div>
    <div class="item" style="top:459px"><h3 class="item__name">Chopped Salad</h3><span class="item__price">$13,00</span><p class="item__desc">Lettuce mix with tomato, onions, peppers, pepperoni, chick peas, fresh mozz, italian herb ving</p></div>
    <div class="item" style="top:515px"><h3 class="item__name">Caesar Salad</h3><span class="item__price">$11,00</span><p class="item__desc">Traditional caesar salad rich and creamy extra shaved parmesan</p></div>
    <div class="item" style="top:559px"><h3 class="item__name">Farm Salad</h3><span class="item__price">$15,00</span><p class="item__desc">Seasonal farmers market salad</p></div>
    <div class="item" style="top:591px"><h3 class="item__name">Grilled Little Gem</h3><span class="item__price">$11,00</span><p class="item__desc">Grilled little gems with bacon, tomato, red onions and blue cheese dressing</p></div>
    <div class="item" style="top:645px"><h3 class="item__name">Spinach and Arugula Salad</h3><span class="item__price">$12,00</span><p class="item__desc">Spinach and argula, red pepperstossed in a lemon ving and housemade croutons</p></div>
    <div class="decor" role="img" aria-label="Faint salad icon" style="left:158px;top:695px;width:44px;height:44px"></div>
  </section>

  <div class="brand-badge"><span class="brand-name">VALDAROSSI’S</span></div>

  <!-- Middle column -->
  <section class="panel panel--pizzas">
    <div class="section-head section-head--large" style="top:37px"><span class="section-head__pill">PIZZAS</span></div>
    <div class="item" style="top:64px"><h3 class="item__name">Margherita</h3><span class="item__price">$14,00</span><p class="item__desc">Classic Margherita pizza - Fresh Mozz Tomato Sauce and Basil</p></div>
    <div class="item" style="top:120px"><h3 class="item__name">Organic Sausage</h3><span class="item__price">$16,00</span><p class="item__desc">Organic Sausage Housemade Red Sauce Mozz hint of fennel</p></div>
    <div class="item" style="top:175px"><h3 class="item__name">Pepperoni</h3><span class="item__price">$16,00</span><p class="item__desc">Harlow Pepperoni - Housemade Red Sauce Chile flakes and Mozz</p></div>
    <div class="item" style="top:231px"><h3 class="item__name">Salumi and Burrata</h3><span class="item__price">$17,00</span><p class="item__desc">Salumi dried Red Sauce finished with whipped burrata</p></div>
    <div class="item" style="top:286px"><h3 class="item__name">Daily special</h3><span class="item__price">$17,00</span><p class="item__desc">Italian fried chicken wings with a kick</p></div>
    <div class="item" style="top:330px"><h3 class="item__name">Mushroom</h3><span class="item__price">$15,00</span><p class="item__desc">Shaved mushrooms with a Parmesan cream and melted onions</p></div>
    <div class="item" style="top:383px"><h3 class="item__name">Prosciutto and egg</h3><span class="item__price">$16,00</span><p class="item__desc">Parma Prosciutto Parmesan cream with Nordvik and gruyere finished with an organic egg</p></div>
    <div class="item" style="top:450px"><h3 class="item__name">Quarttro Formaggi</h3><span class="item__price">$15,00</span><p class="item__desc">Four cheese combination - mozz - fontina - parm cream and gruyere chile flakes and oregano</p></div>
    <div class="item" style="top:517px"><h3 class="item__name">Farmers Pizza</h3><span class="item__price">$17,00</span><p class="item__desc">Seasonal vegatables cream sauce and a variety of cheese</p></div>
    <div class="item" style="top:572px"><h3 class="item__name">Keto friendly</h3><span class="item__price">$17,00</span><p class="item__desc">Cauliflower crust, spinach and kale , parm cream sauce</p></div>
    <div class="decor" role="img" aria-label="Faint pizza slice icon" style="left:80px;top:545px;width:200px;height:110px;border-radius:40px"></div>

    <div class="section-head section-head--small" style="top:727px"><span class="section-head__pill">DAILY SOUP</span></div>
    <div class="item item--plain" style="top:750px"><h3 class="item__name">Example Tomato bisque</h3><span class="item__price">$8,00</span></div>
  </section>

  <!-- Right column -->
  <section class="panel panel--more">
    <div class="section-head section-head--small" style="top:41px"><span class="section-head__pill">SANDWICHES</span></div>
    <div class="item" style="top:58px"><h3 class="item__name">Italian sub</h3><span class="item__price">$13,00</span><p class="item__desc">Prociutto, salumi, turkey, provolone, lettuce, tomato and herb aioli with spicy gardenia</p></div>
    <div class="item" style="top:113px"><h3 class="item__name">Turkey sandwich</h3><span class="item__price">$12,00</span><p class="item__desc">Housemade bread - turkey, cheddar cheese, butter lettuce, tomato and mustard aioli</p></div>
    <div class="item" style="top:169px"><h3 class="item__name">Meatball sub</h3><span class="item__price">$13,00</span><p class="item__desc">Moms meatballs melted provolone on a housemade roll</p></div>
    <div class="item" style="top:224px"><h3 class="item__name">Plantwise burger</h3><span class="item__price">$14,00</span><p class="item__desc">Housemade bun - arugula , tomato, onion and a sundried tomato spread</p></div>
    <div class="item" style="top:280px"><h3 class="item__name">Chicken sandwich</h3><span class="item__price">$13,00</span><p class="item__desc">Fried chicken or chicken breast, provolone, argula, tomato, served with a spicy aioli</p></div>
    <div class="decor" role="img" aria-label="Faint sandwich icon" style="left:147px;top:328px;width:65px;height:62px;border-radius:8px"></div>

    <div class="section-head section-head--small" style="top:428px"><span class="section-head__pill">CRUSTS</span></div>
    <div class="item" style="top:444px"><h3 class="item__name">Traditional</h3><p class="item__desc">Orginal crust you can't miss</p></div>
    <div class="item" style="top:488px"><h3 class="item__name">Gluten free</h3><span class="item__price">$3,00</span><p class="item__desc">Best gluten friendly crust on the west coast</p></div>
    <div class="item" style="top:532px"><h3 class="item__name">Cauliflower</h3><span class="item__price">$3,00</span><p class="item__desc">Vegans have needs</p></div>

    <div class="section-head section-head--small" style="top:610px"><span class="section-head__pill">DIPS</span></div>
    <div class="item item--plain" style="top:627px"><h3 class="item__name">Ranch</h3><span class="item__price">$1,00</span></div>
    <div class="item item--plain" style="top:648px"><h3 class="item__name">Tomato sauce</h3><span class="item__price">$1,00</span></div>
    <div class="item item--plain" style="top:669px"><h3 class="item__name">Spicy dip</h3><span class="item__price">$1,00</span></div>
    <div class="item item--plain" style="top:690px"><h3 class="item__name">Blue cheese</h3><span class="item__price">$1,00</span></div>
    <div class="decor" role="img" aria-label="Faint dip bowl icon" style="left:157px;top:647px;width:65px;height:40px"></div>

    <div class="brand-footer"><span class="brand-name">VALDAROSSI’S</span></div>
  </section>
</div>
</body>
</html>
```